Window Cleaning Flyer targeting body corporates

Need a flyer for window cleaning targeting body corporate (approx A5 print size). It should be professional and match the logo attached.
We are looking to standout but not be to over the top for a window cleaning/services company.
We want to entice the receptionist or managers to call us because they see no good reason not to.

Industry/Entity Type

Window Cleaning

Font styles to use
Serif

Colors
0555a3
fbed22

Requirements
Must have
• Professional with a few of the photos attached included. Must include logo and the following contact details:
• Ph: 9342 6075
• email: admin@brightpane.com.au
• PO Box 4826
• Doncaster East
• 3109
Nice to have
• Colours matching logo/ van print layout. Looking for more of a simplistic professional design.
Should not have
• Cartoon pictures, animated decorations or stock photos.

```html
<!DOCTYPE html>
<html lang="en">
<head>
<meta charset="utf-8">
<title>Bright Pane Window Cleaning – Body Corporate Flyer</title>
<link href="https://fonts.googleapis.com/css2?family=Oswald:wght@400;500;600;700&family=Montserrat:wght@400;500;600;700&display=swap" rel="stylesheet">
<style>
  :root {
    --brand-blue: #0555a3;
    --deep-blue: #0b3f78;
    --brand-yellow: #fbed22;
    --ink: #1c1c1c;
    --white: #ffffff;
    --paper: #f4f6f8;
    --backdrop: #d9dde2;
    --line-blue: #3a72b0;
  }
  * { box-sizing: border-box; margin: 0; padding: 0; }
  html, body { width: 1000px; height: 1200px; overflow: hidden; }
  body { background: var(--backdrop); position: relative; font-family: "Montserrat", Arial, sans-serif; }

  .flyer {
    position: absolute; left: 85px; top: 20px; width: 830px; height: 1160px;
    background: var(--paper); overflow: hidden;
    box-shadow: 0 6px 24px rgba(0,0,0,.25);
  }

  /* header */
  .header {
    position: absolute; left: 0; top: 0; width: 100%; height: 129px;
    background: var(--brand-blue); border-bottom: 5px solid var(--brand-yellow);
  }
  .brand { position: absolute; left: 70px; top: 34px; display: flex; align-items: center; gap: 12px; }
  .brand-mark { width: 20px; height: 20px; border-radius: 50%; background: var(--brand-yellow); }
  .brand-name {
    font-family: "Oswald", sans-serif; font-weight: 600; color: var(--brand-yellow);
    font-size: 36px; line-height: 1; letter-spacing: 1px; text-transform: uppercase;
  }
  .brand-sub {
    position: absolute; left: 102px; top: 80px; font-family: "Oswald", sans-serif; font-weight: 600;
    color: var(--brand-yellow); font-size: 17px; letter-spacing: 1.5px; text-transform: uppercase;
  }
  .experience { position: absolute; right: 70px; top: 26px; display: flex; align-items: center; gap: 10px; }
  .experience-num {
    font-family: "Oswald", sans-serif; font-weight: 700; color: var(--brand-yellow); font-size: 74px; line-height: 1;
  }
  .experience-label { font-family: "Oswald", sans-serif; font-weight: 700; color: var(--brand-yellow); line-height: .95; }
  .experience-label .big { display: block; font-size: 46px; }
  .experience-label .small { display: block; font-size: 22px; }

  /* hero */
  .hero {
    position: absolute; left: 0; top: 143px; width: 100%; height: 522px;
    background: linear-gradient(90deg, #4e6a86 0%, #7f97ad 35%, #c9d3dc 55%, #eef1f4 75%, #f6f7f8 100%);
  }
  .hero-photo { position: absolute; left: 0; top: 0; width: 440px; height: 100%; }
  .quote {
    position: absolute; right: 36px; top: 40px; width: 340px; text-align: right;
    font-family: "Oswald", sans-serif; font-weight: 500; color: var(--ink);
    font-size: 27px; line-height: 1.34;
  }
  .quote .accent { color: var(--brand-blue); font-weight: 600; }
  .quote-mark {
    position: absolute; font-family: "Oswald", sans-serif; font-weight: 700;
    font-size: 90px; color: #8a96a2; line-height: 1; opacity: .7;
  }
  .quote-mark.open { left: 452px; top: 12px; }
  .quote-mark.close { right: 22px; top: 345px; }

  /* photo strip */
  .photo-strip {
    position: absolute; left: 86px; top: 586px; width: 658px; height: 165px;
    border: 5px solid var(--brand-yellow); display: flex; gap: 4px; background: var(--brand-yellow);
    box-shadow: 0 4px 10px rgba(0,0,0,.25);
  }
  .strip-photo { flex: 1; height: 100%; }
  .strip-photo.van { background: linear-gradient(180deg, #dfe5ea, #9aa9b6); }
  .strip-photo.glass { background: linear-gradient(180deg, #4d6d86, #1f3347); }
  .strip-photo.pave { background: linear-gradient(180deg, #7e8c74, #8d8a80); }
  .strip-photo.facade { background: linear-gradient(180deg, #b4865a, #6d7f54); }

  /* services */
  .services {
    position: absolute; left: 79px; top: 786px; width: 694px; height: 200px;
    border: 2px solid var(--line-blue); border-radius: 8px; background: var(--white);
  }
  .services-title {
    position: absolute; left: 172px; top: 765px; width: 500px; height: 46px;
    background: var(--white); border: 2px solid var(--line-blue); border-radius: 8px;
    font-family: "Montserrat", sans-serif; font-weight: 500; font-size: 21px; color: var(--ink);
    display: flex; align-items: center; justify-content: center;
  }
  .service-cols { position: absolute; left: 18px; top: 46px; right: 18px; display: flex; }
  .service-col { flex: 1; padding: 0 10px; font-size: 14px; line-height: 1.3; color: var(--ink); }
  .service-col + .service-col { border-left: 1px solid #c5d3e2; }
  .service-col.center, .service-col.right { text-align: center; }
  .service-item { position: relative; padding-left: 16px; margin-bottom: 12px; }
  .service-item::before {
    content: ""; position: absolute; left: 0; top: 6px; width: 7px; height: 7px; background: var(--brand-blue);
  }
  .service-col.center .service-item::before, .service-col.right .service-item::before { position: static; display: inline-block; margin-right: 6px; vertical-align: 2px; }
  .service-col.center .service-item, .service-col.right .service-item { padding-left: 0; }

  /* call to action */
  .cta {
    position: absolute; left: 130px; top: 960px; width: 570px; height: 116px;
    background: linear-gradient(180deg, #fff7a0, var(--brand-yellow));
    border: 2px solid #d9c800; border-radius: 6px; text-align: center;
    box-shadow: 0 4px 10px rgba(0,0,0,.2);
    display: flex; flex-direction: column; align-items: center; justify-content: center; gap: 2px;
  }
  .cta-phone {
    display: flex; align-items: center; justify-content: center; gap: 10px;
    font-family: "Montserrat", sans-serif; font-weight: 600; font-size: 30px; line-height: 1.2; color: var(--brand-blue);
  }
  .cta-line { font-family: "Montserrat", sans-serif; font-weight: 700; color: var(--ink); line-height: 1.15; text-transform: uppercase; white-space: nowrap; }
  .cta-line.first { font-size: 18px; }
  .cta-line.second { font-size: 25px; }

  /* footer */
  .footer {
    position: absolute; left: 0; top: 1096px; width: 100%; height: 64px; background: var(--brand-blue);
    display: flex; flex-direction: column; align-items: center; justify-content: center; gap: 3px;
    color: var(--white);
  }
  .footer-web { display: flex; align-items: center; gap: 10px; font-size: 19px; font-weight: 500; line-height: 1.1; }
  .footer-contact { font-size: 13px; font-weight: 400; line-height: 1.1; letter-spacing: .3px; }
  .footer-contact .sep { color: var(--brand-yellow); margin: 0 8px; }
</style>
</head>
<body>
  <main class="flyer">
    <header class="header">
      <div class="brand">
        <span class="brand-mark"></span>
        <span class="brand-name">Bright Pane</span>
      </div>
      <div class="brand-sub">Window Cleaning</div>
      <div class="experience">
        <span class="experience-num">15</span>
        <span class="experience-label"><span class="big">YEARS</span><span class="small">OF EXPERIENCE</span></span>
      </div>
    </header>

    <section class="hero">
      <div class="hero-photo" role="img" aria-label="Photo of two uniformed cleaners washing a glass shopfront with extension poles" style="background: linear-gradient(180deg, #5c7891 0%, #35506a 55%, #1e3047 100%);"></div>
      <span class="quote-mark open">&ldquo;</span>
      <p class="quote">Let Bright Pane Take Care Of<br>Your Body Corporate<br>Needs! <span class="accent">WITH OVER<br>15 YEARS OF EXPERIENCE</span><br>We Will Ensure<br>The Job Is Completed<br>To The Highest<br>Standard Everytime..</p>
      <span class="quote-mark close">&rdquo;</span>
    </section>

    <div class="photo-strip">
      <div class="strip-photo van" role="img" aria-label="Photo of the company service van"></div>
      <div class="strip-photo glass" role="img" aria-label="Photo of a cleaner washing building glass"></div>
      <div class="strip-photo pave" role="img" aria-label="Photo of pressure washing a concrete path"></div>
      <div class="strip-photo facade" role="img" aria-label="Photo of a cleaner working on a timber-clad facade"></div>
    </div>

    <section class="services">
      <div class="service-cols">
        <div class="service-col left">
          <p class="service-item">Window Cleaning</p>
          <p class="service-item">Gutter Cleaning (using our ladder free gutter vacuum)</p>
        </div>
        <div class="service-col center">
          <p class="service-item">Pressure Washing including moss treatment to prevent mould regrowth on concrete surface</p>
        </div>
        <div class="service-col right">
          <p class="service-item">Most Importantly, Bright Pane Window Cleaning take pride in being friendly and courteous to all residents.</p>
        </div>
      </div>
    </section>
    <h2 class="services-title">Bright Pane Specialises In Body Corporate</h2>

    <section class="cta">
      <div class="cta-phone">
        <svg width="28" height="28" viewBox="0 0 30 30" aria-hidden="true">
          <circle cx="15" cy="15" r="13" fill="none" stroke="#0555a3" stroke-width="2.5"/>
          <path d="M10.5 8.5c1-.6 1.8-.4 2.3.6l1 2c.3.7.1 1.3-.5 1.8l-.7.5c.6 1.6 1.8 2.9 3.4 3.6l.5-.7c.5-.6 1.1-.8 1.8-.5l2 1c1 .5 1.2 1.3.6 2.3-.8 1.3-2.2 1.9-3.7 1.4-3.6-1.2-6.2-3.8-7.4-7.4-.5-1.5.1-2.9 1.4-3.7z" fill="#0555a3"/>
        </svg>
        <span>(03) 9342 6075</span>
      </div>
      <p class="cta-line first">Contact the Bright Pane team for an easy,</p>
      <p class="cta-line second">Free quote today!</p>
    </section>

    <footer class="footer">
      <div class="footer-web">
        <svg width="18" height="18" viewBox="0 0 18 18" aria-hidden="true">
          <circle cx="9" cy="9" r="7.5" fill="none" stroke="#fff" stroke-width="1.5"/>
          <ellipse cx="9" cy="9" rx="3.2" ry="7.5" fill="none" stroke="#fff" stroke-width="1.2"/>
          <line x1="1.5" y1="9" x2="16.5" y2="9" stroke="#fff" stroke-width="1.2"/>
        </svg>
        <span>www.brightpane-cleaning.com.au</span>
      </div>
      <p class="footer-contact">admin@brightpane.com.au<span class="sep">|</span>PO Box 4826, Doncaster East 3109</p>
    </footer>
  </main>
</body>
</html>
```